New website for actress www.marlene-vogtberg.de

My website is a little old and needs a new look.
I am a german actress who is in the TV and Theaterbusiness.
my chirpnet account is called MarVogtberg
this design will be set up as wordpress site and needs to be optimized for mobile,
so please provide mobile screen views too.
the content will not change much from the excisting site but I would like to have a news section with Videos and press Releases
I would also like my chirpnet feed to be displayed on my landing page.
I am looking forward to your ideas
best regards
marlene

Target Market(s)

press and fans

Industry/Entity Type

Tv

Font styles to use
Serif
Sans Serif

Colors

Designer to choose colors to be used in the design.

Requirements
Must have
• see above

```html
<!DOCTYPE html>
<html lang="de">
<head>
<meta charset="utf-8">
<title>Marlene Vogtberg</title>
<link href="https://fonts.googleapis.com/css2?family=Raleway:wght@300;400&display=swap" rel="stylesheet">
<style>
  :root {
    --rose: #c43a55;
    --rose-hero: #d24a62;
    --rose-dot: #9c1428;
    --ink: #444;
    --muted: #777;
    --rule: #e2e2e2;
    --band: #ebebeb;
    --footer: #5b5b5b;
    --footer-text: #c9c9c9;
    --white: #fff;
  }
  * { margin: 0; padding: 0; box-sizing: border-box; }
  html, body { width: 728px; height: 1200px; overflow: hidden; background: var(--white); }
  body { position: relative; font-family: "Raleway", sans-serif; font-weight: 300; color: var(--ink); }
  .abs { position: absolute; }

  .site-title { top: 22px; left: 0; width: 728px; text-align: center; font-size: 24px; color: var(--rose); }
  .header-rule { top: 59px; left: 24px; width: 640px; height: 1px; background: var(--rule); }
  .main-nav { top: 75px; left: 0; width: 728px; display: flex; justify-content: center; gap: 18px; font-size: 9px; font-weight: 400; color: #333; }
  .main-nav .active { color: var(--rose); }

  .hero { top: 105px; left: 0; width: 728px; height: 275px; background: linear-gradient(90deg, #d44d65 0%, #cf4560 50%, #c93a55 100%); }
  .hero-photo { position: absolute; left: 344px; top: 0; width: 384px; height: 275px; background: radial-gradient(ellipse at 45% 40%, #d8b59a 0%, #b98a5c 30%, #c9455d 70%, #c63a55 100%); }
  .hero-title { position: absolute; left: 30px; top: 90px; font-size: 19px; color: var(--white); font-weight: 300; }
  .hero-text { position: absolute; left: 32px; top: 118px; width: 280px; font-size: 11px; line-height: 15.5px; color: #f1c2ca; }
  .hero-dots { position: absolute; left: 35px; top: 245px; display: flex; gap: 7px; }
  .hero-dots span { width: 8px; height: 8px; border-radius: 50%; background: var(--rose-dot); }
  .hero-dots span:first-child { background: var(--white); }

  .welcome-title { top: 418px; left: 0; width: 728px; text-align: center; font-size: 27px; color: var(--rose); }
  .welcome-text { top: 461px; left: 84px; width: 580px; text-align: center; font-size: 10.4px; line-height: 19.4px; color: var(--muted); }

  .galleries { top: 550px; left: 0; width: 728px; height: 337px; background: var(--band); }
  .gallery-title { position: absolute; top: 18px; font-size: 27px; color: var(--rose); }
  .gallery-frame { position: absolute; top: 67px; width: 288px; height: 205px; }
  .photo-frame { left: 49px; background: linear-gradient(160deg, #4e5a3a 0%, #8d7a5e 40%, #d9b890 55%, #6f8f92 80%, #3a3a3a 100%); }
  .video-frame { left: 386px; background: radial-gradient(ellipse at 55% 45%, #b88a62 0%, #6b4a30 35%, #1d1d1f 75%); }
  .caption { position: absolute; left: 0; bottom: 0; width: 100%; height: 37px; background: rgba(30,30,30,.72); color: var(--white); font-size: 8.5px; font-weight: 400; padding: 5px 0 0 14px; line-height: 15px; }
  .play { position: absolute; left: 116px; top: 75px; }
  .thumbs { position: absolute; top: 284px; }
  .thumb { position: absolute; top: 0; width: 53px; height: 40px; background: linear-gradient(135deg, #c9b59c, #e3cfb1); opacity: .75; }
  .thumb.current { opacity: 1; background: linear-gradient(135deg, #6a4a3a, #d7c0a0 50%, #7fbfbf); }
  .thumb svg { position: absolute; left: 19px; top: 12px; }
  .arrow { position: absolute; top: 0; font-size: 22px; color: #555; font-weight: 400; line-height: 40px; }

  .feeds-title { top: 910px; left: 0; width: 728px; text-align: center; font-size: 27px; color: var(--rose); }
  .avatar { top: 976px; left: 64px; width: 76px; height: 60px; background: radial-gradient(ellipse at 50% 45%, #e6c6a0, #b88d50 60%, #d9d2c4); }
  .tweet { top: 974px; left: 152px; width: 510px; font-size: 7.4px; line-height: 15.3px; color: #555; font-weight: 400; }
  .tweet .date { color: #999; }
  .tweet-actions { top: 1041px; left: 155px; display: flex; gap: 10px; font-size: 9px; font-weight: 400; color: var(--rose); }
  .tweet-nav { top: 1034px; left: 617px; font-size: 20px; color: #444; font-weight: 400; letter-spacing: 2px; }

  .site-footer { top: 1071px; left: 0; width: 728px; height: 129px; background: var(--footer); }
  .footer-nav { position: absolute; top: 27px; left: 0; width: 728px; display: flex; justify-content: center; gap: 18px; font-size: 9px; color: var(--footer-text); }
  .copyright { position: absolute; top: 58px; left: 0; width: 728px; text-align: center; font-size: 8.5px; color: var(--footer-text); }
  .social { position: absolute; top: 92px; left: 0; width: 728px; display: flex; justify-content: center; gap: 12px; font-size: 8.5px; font-weight: 400; color: var(--white); }
  .social span { display: flex; align-items: center; gap: 4px; }
  .social span::before { content: ""; width: 9px; height: 9px; background: #8a8a8a; }
</style>
</head>
<body>
  <header>
    <h1 class="abs site-title" style="font-weight:300">Marlene Vogtberg</h1>
    <div class="abs header-rule"></div>
    <nav class="abs main-nav">
      <span class="active">HOME</span><span>BIOGRAPHIE</span><span>INTERVIEW</span><span>PRIVATE PHOTOS</span><span>EROTIC PHOTOS</span><span>AUTOGRAMME</span><span>CHARITY</span><span>CONTACT</span>
    </nav>
  </header>

  <section class="abs hero">
    <div class="hero-photo" role="img" aria-label="Portrait of the actress with curly blonde hair at a red-carpet event"></div>
    <h2 class="hero-title">LOREM IPSUM DOLOR SIT AMET</h2>
    <p class="hero-text">Consectetur adipisicing elit, sed do eiusmod tempor incididunt ut labore et dolore magna aliqua. Ut enim ad minim veniam, quis nostrud exercitation ullamco laboris nisi ut aliquip ex ea commodo consequat.</p>
    <div class="hero-dots"><span></span><span></span><span></span><span></span><span></span></div>
  </section>

  <h2 class="abs welcome-title" style="font-weight:300">Welcome to Marlene Vogtberg</h2>
  <p class="abs welcome-text">Consectetur adipisicing elit, sed do eiusmod tempor incididunt ut labore et dolore magna aliqua. Ut enim ad minim veniam, quis nostrud exercitation ullamco laboris nisi ut aliquip ex ea commodo consequat.Consectetur adipisicing elit, sed do eius-mod tempor incididunt ut labore et dolore magna aliqua. Ut enim ad minim veniam, quis nostrud exercitation ullamco.</p>

  <section class="abs galleries">
    <h2 class="gallery-title" style="left:50px;font-weight:300">Photo Gallery</h2>
    <h2 class="gallery-title" style="left:386px;font-weight:300">Video Gallery</h2>

    <div class="gallery-frame photo-frame" role="img" aria-label="Photo of the actress in a turquoise dress at an outdoor event">
      <div class="caption">Jan 26 2013<br>Lorem ipsum dolor sit amet</div>
    </div>
    <div class="gallery-frame video-frame" role="img" aria-label="Video still of the actress in an interview">
      <svg class="play" width="50" height="50" viewBox="0 0 50 50"><circle cx="25" cy="25" r="23" fill="rgba(0,0,0,.35)" stroke="#fff" stroke-width="2.5"/><path d="M19 14 L36 25 L19 36 Z" fill="#fff"/></svg>
    </div>

    <div class="thumbs" style="left:0">
      <span class="arrow" style="left:52px">‹</span>
      <div class="thumb current" style="left:74px" role="img" aria-label="Photo thumbnail"></div>
      <div class="thumb" style="left:134px" role="img" aria-label="Photo thumbnail"></div>
      <div class="thumb" style="left:198px" role="img" aria-label="Photo thumbnail"></div>
      <div class="thumb" style="left:258px" role="img" aria-label="Photo thumbnail"></div>
      <span class="arrow" style="left:320px">›</span>
    </div>
    <div class="thumbs" style="left:0">
      <span class="arrow" style="left:393px">‹</span>
      <div class="thumb current" style="left:414px" role="img" aria-label="Video thumbnail"><svg width="16" height="16" viewBox="0 0 16 16"><circle cx="8" cy="8" r="7" fill="rgba(255,255,255,.5)" stroke="#333"/><path d="M6 4.5 L11 8 L6 11.5Z" fill="#333"/></svg></div>
      <div class="thumb" style="left:475px" role="img" aria-label="Video thumbnail"><svg width="16" height="16" viewBox="0 0 16 16"><circle cx="8" cy="8" r="7" fill="rgba(255,255,255,.5)" stroke="#333"/><path d="M6 4.5 L11 8 L6 11.5Z" fill="#333"/></svg></div>
      <div class="thumb" style="left:538px" role="img" aria-label="Video thumbnail"><svg width="16" height="16" viewBox="0 0 16 16"><circle cx="8" cy="8" r="7" fill="rgba(255,255,255,.5)" stroke="#333"/><path d="M6 4.5 L11 8 L6 11.5Z" fill="#333"/></svg></div>
      <div class="thumb" style="left:598px" role="img" aria-label="Video thumbnail"><svg width="16" height="16" viewBox="0 0 16 16"><circle cx="8" cy="8" r="7" fill="rgba(255,255,255,.5)" stroke="#333"/><path d="M6 4.5 L11 8 L6 11.5Z" fill="#333"/></svg></div>
      <span class="arrow" style="left:660px">›</span>
    </div>
  </section>

  <h2 class="abs feeds-title" style="font-weight:300">Chirpnet Feeds</h2>
  <div class="abs avatar" role="img" aria-label="Profile photo of the actress"></div>
  <div class="abs tweet">
    <div class="date">Jan 27, 2014</div>
    <div>Marlene Vogtberg @MarVogtberg</div>
    <div>"@Nordblatt_HH: Nach 18 Jahren Flucht: Auftrags-Killerin Estelle in #Hamburg gefasst http://www.nordblatt.de/regional/hamburg/terror-<br>gruppen/auftrags-killerin-estelle-in-hamburg-gefasst-34409756.nordblatt.html .." was wollte sie in Hamburg?</div>
  </div>
  <div class="abs tweet-actions"><span>Reply</span><span>Retweet</span><span>Favorite</span></div>
  <div class="abs tweet-nav">‹›</div>

  <footer class="abs site-footer">
    <nav class="footer-nav">
      <span>HOME</span><span>BIOGRAPHIE</span><span>INTERVIEW</span><span>PRIVATE PHOTOS</span><span>EROTIC PHOTOS</span><span>AUTOGRAMME</span><span>CHARITY</span><span>CONTACT</span>
    </nav>
    <p class="copyright">ALL RIGHTS RESERVED. COPYRIGHTS @ 2013</p>
    <div class="social"><span>Friendbook</span><span>Chirpnet</span><span>Linkhub</span><span>RSS</span><span>Plusring</span></div>
  </footer>
</body>
</html>
```